We need a DL size flyer, double sided, for our lawn mowing and gardening business, Kestrel Greens.

We want to run on the front side, the following promotion:
50% off lawn mowing, applies to first lawn mowed on any regular service,
applies to first 100 callers only, so call now!
Professional lawn mowing at an affordable price.

Logo at the bottom left, with Lawn and Garden Maintenance written just below logo.

On bottom Right contact details;
Tom and Gareth
Ph: 0487650912
Email: kestrelgreens@mailbox-example.com
www.kestrelgreens-example.com.au

Front side positioned horizontally, with a bright and colour full design in the background, with the offer of 50% Off lawn mowing in large letters along the top.

On the rear side, also positioned horizontally, a list of our services, stating;

At Kestrel Greens we specialise in the following services;
Lawn mowing
Edging
Blowing
Hedging
Pruning
Tree Loping
Weeding
Poisoning
Mulching
Fertilising
Rubbish removal
Planting
Lawn care and advice
Turf
And any other garden maintenance job,
No job too big or too small.
(No particular order, whatever fits best)
Also include our contact details,
Kestrel Greens
Ph 0487650912
www.kestrelgreens-example.com.au

Target Market(s)

Home owners, aged between 30-50 years old, moderate socio ecenomic status to more afluent areas.

Industry/Entity Type

Business

Requirements
Must have
• DL size, front and back, full colour.
Nice to have
• The writting stating "Kestrel Greens" in our logo is quite bland, if that could also be amended to make it more appealing, but change the writting design only not the actual logo.

```html
<!DOCTYPE html>
<html lang="en">
<head>
<meta charset="utf-8">
<title>Kestrel Greens – DL Flyer</title>
<link rel="stylesheet" href="https://fonts.googleapis.com/css2?family=Maven+Pro:wght@400;500;700&family=Roboto+Condensed:wght@700&display=swap">
<style>
  :root {
    --page-bg: #ececec;
    --headline-green: #7cb94a;
    --tab-green: #1f9a4a;
    --sun-yellow: #f6cd1f;
    --sky-top: #f4fbfb;
    --sky-bottom: #cfeceb;
    --grass-light: #9fd54a;
    --grass-dark: #2f7d1e;
    --back-bg: #c7e6e5;
    --leaf-light: #b8d98a;
    --leaf-dark: #3f6e2a;
    --ink: #161616;
    --white: #ffffff;
  }
  * { box-sizing: border-box; margin: 0; padding: 0; }
  html, body { width: 1200px; height: 800px; overflow: hidden; }
  body {
    background: var(--page-bg);
    position: relative;
    font-family: "Maven Pro", "Trebuchet MS", sans-serif;
    color: var(--ink);
  }
  .flyer {
    position: absolute;
    width: 793px;
    height: 374px;
    overflow: hidden;
  }
  /* ---------- Front ---------- */
  .flyer--front {
    left: 151px; top: 33px;
    background: linear-gradient(180deg, var(--sky-top) 0%, var(--sky-bottom) 45%, #e9f6f2 55%);
  }
  .front__grass {
    position: absolute; left: 0; right: 0; top: 150px; bottom: 0;
    background: linear-gradient(180deg, rgba(159,213,74,0) 0%, var(--grass-light) 18%, #5fae2c 55%, var(--grass-dark) 100%);
  }
  .offer { position: absolute; left: 0; right: 0; top: 24px; text-align: center; color: var(--headline-green); }
  .offer__headline { font-size: 56px; font-weight: 400; line-height: 1; letter-spacing: 1px; }
  .offer__terms { font-size: 33px; font-weight: 400; line-height: 1.1; margin-top: 6px; }
  .brand {
    position: absolute; left: 36px; top: 250px; width: 227px;
    text-align: center;
  }
  .brand__name { font-size: 25px; font-weight: 700; color: var(--white); white-space: nowrap; }
  .brand__tagline {
    position: absolute; left: 36px; width: 227px; top: 310px;
    text-align: center; color: var(--white); font-size: 18px; font-weight: 500; line-height: 1.25;
  }
  .promo-tab {
    position: absolute; left: 445px; top: 144px; width: 304px; height: 65px;
    background: var(--tab-green); border-top-right-radius: 22px;
    color: var(--white); font-family: "Roboto Condensed", "Arial Narrow", sans-serif;
    font-size: 20px; font-weight: 700; line-height: 1.2; padding: 9px 0 0 12px;
  }
  .contact-box {
    position: absolute; background: var(--sun-yellow);
    border-top-left-radius: 40px; text-align: center;
  }
  .flyer--front .contact-box { left: 445px; top: 220px; width: 348px; height: 113px; padding-top: 12px; }
  .contact-box__name { font-size: 20px; font-weight: 500; line-height: 1.25; }
  .contact-box__line { font-size: 16px; line-height: 1.3; }
  /* ---------- Back ---------- */
  .flyer--back { left: 263px; top: 391px; background: var(--back-bg); }
  .back__photo {
    position: absolute; left: 477px; top: 0; right: 0; bottom: 0;
    background: radial-gradient(ellipse at 40% 35%, var(--leaf-light) 0%, #7aa652 45%, var(--leaf-dark) 100%);
    border-bottom-left-radius: 60px 120px;
  }
  .services-tab {
    position: absolute; left: 44px; top: 36px; width: 400px; height: 64px;
    background: var(--tab-green); border-top-right-radius: 22px;
    color: var(--white); font-family: "Roboto Condensed", "Arial Narrow", sans-serif;
    font-size: 22px; font-weight: 700; line-height: 1.2; padding: 7px 0 0 12px;
  }
  .service-col { position: absolute; top: 113px; font-size: 17px; line-height: 22.4px; }
  .service-col--one { left: 44px; }
  .service-col--two { left: 240px; width: 185px; }
  .service-list { list-style: none; }
  .service-list li { position: relative; padding-left: 22px; }
  .service-list li::before { content: "•"; position: absolute; left: 0; }
  .service-note strong { font-weight: 700; }
  .flyer--back .contact-box { left: 475px; top: 209px; width: 318px; height: 127px; padding-top: 20px; }
</style>
</head>
<body>
  <section class="flyer flyer--front">
    <div class="front__grass" role="img" aria-label="Photo of tall fresh green lawn grass"></div>
    <header class="offer">
      <h1 class="offer__headline">50% OFF LAWN MOWING</h1>
      <p class="offer__terms">applies to first 100 callers only, so call now</p>
    </header>
    <div class="brand"><span class="brand__name">Kestrel Greens</span></div>
    <p class="brand__tagline">Lawn and Garden<br>Maintenance</p>
    <div class="promo-tab">PROFESSIONAL LAWN MOWING<br>AT AN AFFORDABLE PRICE.</div>
    <div class="contact-box">
      <p class="contact-box__name">Tom and Gareth</p>
      <p class="contact-box__line">Ph: 0487650912</p>
      <p class="contact-box__line">kestrelgreens@mailbox-example.com</p>
      <p class="contact-box__line">www.kestrelgreens-example.com.au</p>
    </div>
  </section>

  <section class="flyer flyer--back">
    <div class="back__photo" role="img" aria-label="Photo of garden secateurs pruning a leafy branch"></div>
    <div class="services-tab">AT KESTREL GREENS WE SPECIALISE<br>IN THE FOLLOWING SERVICES:</div>
    <div class="service-col service-col--one">
      <ul class="service-list">
        <li>Lawn mowing</li><li>Edging</li><li>Blowing</li><li>Hedging</li><li>Pruning</li>
        <li>Tree Loping</li><li>Weeding</li><li>Poisoning</li><li>Mulching</li><li>Fertilising</li>
      </ul>
    </div>
    <div class="service-col service-col--two">
      <ul class="service-list">
        <li>Rubbish removal</li><li>Planting</li><li>Lawn care and<br>advice</li><li>Turf</li>
      </ul>
      <p class="service-note">...and any other garden maintenance job. <strong>No job too big or too small.</strong></p>
    </div>
    <div class="contact-box">
      <p class="contact-box__name">Kestrel Greens</p>
      <p class="contact-box__line">Ph 0487650912</p>
      <p class="contact-box__line">www.kestrelgreens-example.com.au</p>
    </div>
  </section>
</body>
</html>
```